Bright Path Flyer Design for Virtual Online Clinic. -5.5 x 8.5 inches (half sheet)

We need a clean, modern flyer design for Bright Path, a new virtual walk-in clinic based in British Columbia. The flyer will be used in libraries, pharmacies, and community centers to help residents easily access primary care through their Bright Path NFC access card.
The flyer will ask a question : NEED A DOCTOR? This should be large and attention grabbing.
The design should clearly feature a Bright Path card image (the access card) as the centerpiece and visually show how patients can use it to book appointments. The tone should feel trustworthy, healthcare-oriented, and community-friendly — clean fonts, clear spacing, and strong readability from a distance.

Side One: This card has the NFC Access Card.
NEED A DOCTOR? (Large Font, Attention Grabbing)
How to Book an Appointment using your Bright Path Card
Step 1: Tap Your Card on Your Phone
Hold your card near the back of your phone.
It will activate automatically — no app needed.
The Bright Path scheduler will open.
Step 2: Schedule Your Appointment
Select your clinical concern.
Choose your time window.
Register (only once).
Confirm your appointment.
Step 3: Relax, we’ll take care of the rest
A doctor will call during your scheduled time.
Once booked, you’ll be able to call our office.
No emails, no texts — just a real person.
It’s that simple.
Side Two:
About Bright Path
Created by Dr. Marcus Ferrigan
Bright Path was founded to make healthcare simple and convenient. Prescription renewals. Common infections. Medical notes. And so much more.
Our doctors can address 120+ health concerns virtually — providing quality care without the waiting room. No waiting rooms. Just real doctors providing real care.
Why Patients Choose Bright Path
Easy access – book and be seen from anywhere in BC.
Effortless booking – tap your Bright Path Card to begin.
Trusted physicians – every visit is with a licensed BC family doctor.
How It Works
Book your visit — choose a time window that fits your day.
Join the queue — you’ll be called when it’s your turn.
Speak directly with your doctor — simple, secure, and stress-free.
Convenient Care for Common Concerns

Additional Details.
Please find the domain to be launched soon. I've attached the NFC card file for review, it is 85.5 mm x 54 mm. The card will be glued to the flyer.
I've attached examples of flyers but they are not the look I am seeking and I am looking for creative solutions.
Thank you!
http://brightpath-example.test/

Adult Patients in British Columbia

Healthcare

• Looking for clean lines, uniform appearance, and high legibility i.e poppins

0054AA
0677BA
7BADD7
CADEEF
E8F1F8

• Need A Doctor?
• Elegant style, not too busy, clear layout.
• Clutter, look cheap - review examples.

```html
<!DOCTYPE html>
<html lang="en">
<head>
<meta charset="utf-8">
<title>Bright Path Flyer – Presentation Board</title>
<link rel="stylesheet" href="https://fonts.googleapis.com/css2?family=Montserrat:wght@200;500;600;700;800;900&family=Source+Sans+3:wght@600;700&display=swap">
<style>
:root{
  --board:#86a5a2;
  --navy:#263a84;
  --navy-deep:#1f3173;
  --blue:#0a8dc6;
  --yellow:#f2e24a;
  --yellow-soft:#f8f1b8;
  --cream:#fcf9e6;
  --ink:#1c1c1c;
  --lavender:#c5c8df;
  --annot:#2a2a2a;
}
*{box-sizing:border-box;margin:0;padding:0}
html,body{width:901px;height:1200px;overflow:hidden}
body{background:var(--board);position:relative;font-family:"Montserrat",sans-serif;color:var(--navy)}

/* ---------- board annotations ---------- */
.dim-line{position:absolute;background:var(--annot)}
.dim-line--height{left:42px;top:54px;width:1px;height:573px}
.dim-line--width{left:63px;top:644px;width:364px;height:1px}
.dim-label{position:absolute;font-family:"Source Sans 3",sans-serif;font-weight:700;color:var(--annot);font-size:18px;white-space:nowrap}
.dim-label--height{left:28px;top:332px;transform:translate(-50%,-50%) rotate(-90deg)}
.dim-label--width{left:258px;top:667px;transform:translate(-50%,-50%)}
.card-slot{position:absolute;left:122px;top:756px;width:192px;height:113px;background:#fff;border-radius:6px}
.card-slot__label{position:absolute;left:223px;top:907px;transform:translate(-50%,-50%);font-family:"Source Sans 3",sans-serif;font-weight:700;font-size:17px;color:var(--annot);white-space:nowrap}
.guide-arrow{position:absolute;left:0;top:0;width:901px;height:1200px;pointer-events:none;z-index:5}

/* ---------- flyer shell ---------- */
.flyer{position:absolute;width:383px;height:592px;overflow:hidden;background:#fff}
.flyer--front-a{left:56px;top:44px}
.flyer--back{left:462px;top:44px}
.flyer--front-b{left:372px;top:699px;transform:scale(0.81);transform-origin:0 0}

.flyer__sky{position:absolute;inset:0 0 auto 0;height:320px;
  background:linear-gradient(180deg,var(--navy) 0%,#2e4390 28%,#6e7fb8 48%,#cdd3ea 66%,#fff 82%)}
.flyer__welcome{position:absolute;top:38px;left:0;right:0;text-align:center;color:var(--yellow);font-weight:800;font-size:18px;letter-spacing:.3px}

.access-card{position:absolute;left:70px;top:81px;width:244px;height:139px;border-radius:6px;
  background:linear-gradient(90deg,var(--navy) 0%,var(--navy) 24%,#ffffff 24%,#f3f4f8 100%)}

.headline{position:absolute;top:232px;left:0;right:0;text-align:center;font-weight:900;font-size:38px;letter-spacing:-.5px;color:var(--navy)}

.meadow{position:absolute;left:0;right:0;top:313px;height:236px;border-radius:60px 60px 0 0;
  background:linear-gradient(180deg,#f1e676 0%,var(--yellow-soft) 45%,var(--cream) 100%)}

.booking-title{position:absolute;left:69px;top:295px;width:245px;height:36px;border-radius:18px;background:var(--navy);
  color:var(--yellow);text-align:center;font-weight:700;font-size:12.5px;line-height:16px;padding-top:2px;z-index:2}
.booking-rule{position:absolute;left:49px;top:312px;width:287px;height:2px;background:var(--navy)}

.step{position:absolute;left:35px;width:315px;border-bottom:1px solid var(--navy)}
.step--one{top:344px;height:55px}
.step--two{top:410px;height:55px}
.step--three{top:477px;height:60px}
.step__label{position:absolute;left:0;bottom:8px;font-weight:800;font-size:9.5px}
.step__numeral{position:absolute;left:16px;bottom:-6px;font-weight:200;font-size:58px;line-height:1;color:transparent;-webkit-text-stroke:1.2px var(--navy)}
.step__icon{position:absolute;left:64px;top:2px;width:36px;height:48px}
.step__heading{position:absolute;left:110px;top:0;font-weight:800;font-size:10.2px;white-space:nowrap}
.step__list{position:absolute;left:110px;top:14px;width:218px;display:grid;grid-template-columns:117px 101px;row-gap:2px;list-style:none}
.tick{position:relative;padding-left:14px;font-weight:500;font-size:6.8px;line-height:8px;color:#2b2b2b}
.tick::before{content:"✓";position:absolute;left:0;top:0;width:8px;height:8px;border:1px solid var(--navy);border-radius:50%;
  font-size:6.5px;line-height:7px;text-align:center;color:var(--navy);font-weight:800}

.help-bar{position:absolute;left:0;right:0;top:549px;height:35px;background:var(--yellow)}
.help-bar__note{position:absolute;left:0;top:0;width:184px;height:35px;background:var(--navy);
  clip-path:polygon(0 0,100% 0,94% 100%,0 100%);color:var(--yellow);font-weight:500;font-size:6.9px;line-height:10px;padding:8px 0 0 21px;white-space:nowrap}
.help-bar__email{position:absolute;left:191px;top:9px;font-weight:700;font-size:12.5px;color:var(--navy);white-space:nowrap}

/* ---------- back side ---------- */
.flyer__haze{position:absolute;inset:0;background:linear-gradient(180deg,var(--lavender) 0%,#eceef6 20%,#fff 32%)}
.about-title{position:absolute;top:30px;left:0;font-weight:800;font-size:25px;white-space:nowrap}
.about-title__mark{display:inline-block;background:var(--yellow);color:#111;padding:0 3px 0 41px}
.about-title__brand{color:var(--navy);padding-left:3px}
.about-copy{position:absolute;left:41px;top:63px;width:262px;font-weight:500;font-size:8.9px;line-height:11.5px;color:var(--ink)}
.about-copy p+p{margin-top:6px}
.back-meadow{position:absolute;left:0;right:0;top:276px;height:273px;border-radius:70px 70px 0 0;
  background:linear-gradient(180deg,#f1e676 0%,var(--yellow-soft) 40%,var(--cream) 100%)}
.product-shot{position:absolute;left:29px;top:146px;width:321px;height:189px;border-radius:10px;
  background:linear-gradient(160deg,#e4e4e6 0%,#c9c9cd 45%,#34478d 70%,var(--navy) 100%)}

.reasons{position:absolute;left:37px;top:349px;width:160px}
.reasons__title{font-weight:800;font-size:14.2px;line-height:15px;letter-spacing:.3px}
.reason{position:absolute;left:0;width:160px}
.reason--access{top:54px}.reason--booking{top:95px}.reason--trust{top:146px}
.reason__icon{position:absolute;left:0;top:0;width:32px;height:32px;border-radius:6px;background:linear-gradient(135deg,var(--yellow),var(--navy))}
.reason__name{margin-left:42px;font-weight:800;font-size:10.2px;line-height:11px}
.reason__text{margin-left:42px;margin-top:2px;font-weight:500;font-size:8px;line-height:10.5px;color:var(--ink)}

.how-box{position:absolute;left:203px;top:346px;width:155px;height:190px;border-radius:12px;
  background:linear-gradient(180deg,var(--navy) 0%,#1d5a9e 60%,var(--blue) 100%);padding:10px 9px 0 10px}
.how-box__title{font-weight:800;font-size:14.2px;color:var(--yellow);letter-spacing:.5px}
.how-item{position:absolute;left:10px;width:140px;padding-left:25px;font-weight:500;font-size:8.5px;line-height:11.3px;color:#fff}
.how-item strong{color:var(--yellow);font-weight:700}
.how-item::before{content:"✓";position:absolute;left:0;top:1px;width:16px;height:16px;border:1.5px solid var(--yellow);border-radius:50%;
  color:var(--yellow);font-size:11px;line-height:13px;text-align:center;font-weight:800}
.how-item--book{top:28px}.how-item--queue{top:70px}.how-item--speak{top:112px}.how-item--care{top:154px}
</style>
</head>
<body>

<!-- Front, with printed card -->
<section class="flyer flyer--front-a" aria-label="Front side with access card">
  <div class="flyer__sky"></div>
  <p class="flyer__welcome">WELCOME TO Bright Path</p>
  <div class="access-card" role="img" aria-label="Bright Path NFC access card artwork"></div>
  <h1 class="headline">NEED A DOCTOR?</h1>
  <div class="meadow"></div>
  <div class="booking-rule"></div>
  <h2 class="booking-title">How to Book an Appointment<br>using your Bright Path Card</h2>

  <div class="step step--one">
    <span class="step__label">STEP</span><span class="step__numeral">1</span>
    <svg class="step__icon" viewBox="0 0 36 48" aria-hidden="true"><rect x="3" y="2" width="22" height="44" rx="4" fill="#fff" stroke="#263a84" stroke-width="2"/><text x="6" y="20" font-family="Montserrat,sans-serif" font-weight="800" font-size="8" fill="#263a84">NFC</text><rect x="15" y="26" width="19" height="12" rx="2" fill="#f2e24a" stroke="#263a84" stroke-width="1.5"/></svg>
    <h3 class="step__heading">TAP YOUR CARD ON YOUR PHONE</h3>
    <ul class="step__list">
      <li class="tick">Hold your card near the<br>back of your phone.</li>
      <li class="tick">The Bright Path<br>scheduler will open.</li>
      <li class="tick">It will activate automatically<br>— no app needed.</li>
    </ul>
  </div>
  <div class="step step--two">
    <span class="step__label">STEP</span><span class="step__numeral">2</span>
    <svg class="step__icon" viewBox="0 0 36 48" aria-hidden="true"><rect x="6" y="2" width="24" height="44" rx="4" fill="#f2e24a" stroke="#263a84" stroke-width="2"/><rect x="10" y="14" width="16" height="14" fill="#fff" stroke="#263a84" stroke-width="1.5"/><line x1="10" y1="18" x2="26" y2="18" stroke="#263a84" stroke-width="1.5"/></svg>
    <h3 class="step__heading">SCHEDULE YOUR APPOINTMENT</h3>
    <ul class="step__list">
      <li class="tick">Select your<br>clinical concern.</li>
      <li class="tick">Register<br>(only once).</li>
      <li class="tick">Choose your<br>time window.</li>
      <li class="tick">Confirm your<br>appointment.</li>
    </ul>
  </div>
  <div class="step step--three">
    <span class="step__label">STEP</span><span class="step__numeral">3</span>
    <div class="step__icon" role="img" aria-label="Doctor on a phone call illustration" style="background:linear-gradient(135deg,#f2e24a,#263a84);border-radius:6px;height:40px"></div>
    <h3 class="step__heading">RELAX, WE’LL TAKE CARE OF THE REST</h3>
    <ul class="step__list">
      <li class="tick">A doctor will call during<br>your scheduled time.</li>
      <li class="tick">No emails, no texts —<br>just a real person.</li>
      <li class="tick">Once booked, you’ll be<br>able to call our office.</li>
      <li class="tick">It’s that simple.</li>
    </ul>
  </div>

  <footer class="help-bar">
    <p class="help-bar__note">If you’re having trouble with your card<br>or the access page, We’re here to help:</p>
    <p class="help-bar__email">support@brightpathbc.test</p>
  </footer>
</section>

<!-- Back -->
<section class="flyer flyer--back" aria-label="Back side about the clinic">
  <div class="flyer__haze"></div>
  <h2 class="about-title"><span class="about-title__mark">About</span><span class="about-title__brand">Bright Path</span></h2>
  <div class="about-copy">
    <p>Bright Path was founded to make healthcare simple and convenient. Prescription renewals. Common infections. Medical notes. And so much more.</p>
    <p>Our doctors can address 120+ health concerns virtually — providing quality care without the waiting room. No waiting rooms. Just real doctors providing real care.</p>
  </div>
  <div class="back-meadow"></div>
  <div class="product-shot" role="img" aria-label="Photo of Bright Path access cards beside a marble block and sphere"></div>

  <div class="reasons">
    <h3 class="reasons__title">WHY PATIENTS<br>CHOOSE<br>BRIGHT PATH</h3>
    <div class="reason reason--access">
      <div class="reason__icon" role="img" aria-label="Hand tapping a phone icon"></div>
      <p class="reason__name">EASY ACCESS</p>
      <p class="reason__text">book and be seen from anywhere in BC.</p>
    </div>
    <div class="reason reason--booking">
      <div class="reason__icon" role="img" aria-label="Booking button icon"></div>
      <p class="reason__name">EFFORTLESS<br>BOOKING</p>
      <p class="reason__text">Tap your Bright Path Card to begin.</p>
    </div>
    <div class="reason reason--trust">
      <div class="reason__icon" role="img" aria-label="Approval rosette icon"></div>
      <p class="reason__name">TRUSTED<br>PHYSICIANS</p>
      <p class="reason__text">Every visit is with a licensed BC family doctor.</p>
    </div>
  </div>

  <div class="how-box">
    <h3 class="how-box__title">HOW IT WORKS</h3>
    <p class="how-item how-item--book"><strong>Book your visit</strong> — choose a time window that fits your day.</p>
    <p class="how-item how-item--queue"><strong>Join the queue</strong> — you’ll be called when it’s your turn.</p>
    <p class="how-item how-item--speak"><strong>Speak directly with your doctor</strong> — simple, secure, and stress-free.</p>
    <p class="how-item how-item--care">Convenient Care for Common Concerns</p>
  </div>

  <footer class="help-bar">
    <p class="help-bar__note">If you’re having trouble with your card<br>or the access page, We’re here to help:</p>
    <p class="help-bar__email">support@brightpathbc.test</p>
  </footer>
</section>

<!-- Front, card applied by hand -->
<section class="flyer flyer--front-b" aria-label="Front side with space for the glued card">
  <div class="flyer__sky"></div>
  <p class="flyer__welcome">WELCOME TO Bright Path</p>
  <h1 class="headline">NEED A DOCTOR?</h1>
  <div class="meadow"></div>
  <div class="booking-rule"></div>
  <h2 class="booking-title">How to Book an Appointment<br>using your Bright Path Card</h2>

  <div class="step step--one">
    <span class="step__label">STEP</span><span class="step__numeral">1</span>
    <svg class="step__icon" viewBox="0 0 36 48" aria-hidden="true"><rect x="3" y="2" width="22" height="44" rx="4" fill="#fff" stroke="#263a84" stroke-width="2"/><text x="6" y="20" font-family="Montserrat,sans-serif" font-weight="800" font-size="8" fill="#263a84">NFC</text><rect x="15" y="26" width="19" height="12" rx="2" fill="#f2e24a" stroke="#263a84" stroke-width="1.5"/></svg>
    <h3 class="step__heading">TAP YOUR CARD ON YOUR PHONE</h3>
    <ul class="step__list">
      <li class="tick">Hold your card near the<br>back of your phone.</li>
      <li class="tick">The Bright Path<br>scheduler will open.</li>
      <li class="tick">It will activate automatically<br>— no app needed.</li>
    </ul>
  </div>
  <div class="step step--two">
    <span class="step__label">STEP</span><span class="step__numeral">2</span>
    <svg class="step__icon" viewBox="0 0 36 48" aria-hidden="true"><rect x="6" y="2" width="24" height="44" rx="4" fill="#f2e24a" stroke="#263a84" stroke-width="2"/><rect x="10" y="14" width="16" height="14" fill="#fff" stroke="#263a84" stroke-width="1.5"/><line x1="10" y1="18" x2="26" y2="18" stroke="#263a84" stroke-width="1.5"/></svg>
    <h3 class="step__heading">SCHEDULE YOUR APPOINTMENT</h3>
    <ul class="step__list">
      <li class="tick">Select your<br>clinical concern.</li>
      <li class="tick">Register<br>(only once).</li>
      <li class="tick">Choose your<br>time window.</li>
      <li class="tick">Confirm your<br>appointment.</li>
    </ul>
  </div>
  <div class="step step--three">
    <span class="step__label">STEP</span><span class="step__numeral">3</span>
    <div class="step__icon" role="img" aria-label="Doctor on a phone call illustration" style="background:linear-gradient(135deg,#f2e24a,#263a84);border-radius:6px;height:40px"></div>
    <h3 class="step__heading">RELAX, WE’LL TAKE CARE OF THE REST</h3>
    <ul class="step__list">
      <li class="tick">A doctor will call during<br>your scheduled time.</li>
      <li class="tick">No emails, no texts —<br>just a real person.</li>
      <li class="tick">Once booked, you’ll be<br>able to call our office.</li>
      <li class="tick">It’s that simple.</li>
    </ul>
  </div>

  <footer class="help-bar">
    <p class="help-bar__note">If you’re having trouble with your card<br>or the access page, We’re here to help:</p>
    <p class="help-bar__email">support@brightpathbc.test</p>
  </footer>
</section>

<!-- Board notes -->
<div class="dim-line dim-line--height"></div>
<span class="dim-label dim-label--height">8.5 inch Width</span>
<div class="dim-line dim-line--width"></div>
<span class="dim-label dim-label--width">5.5 inch Width</span>
<div class="card-slot"></div>
<span class="card-slot__label">Real Card goes here</span>
<svg class="guide-arrow" viewBox="0 0 901 1200" aria-hidden="true">
  <path d="M174 885 Q 300 895 380 887 Q 470 872 520 835" fill="none" stroke="#f2e24a" stroke-width="2" stroke-dasharray="6 5"/>
  <polygon points="514,822 536,818 526,840" fill="#f2e24a"/>
</svg>

</body>
</html>
```